Flyer back 2 school

Copper Fade 9th annual back 2 school drive
Saturday July 31 12–5pm
Free School Supplies, Games, entertainment, free food

To volunteer or donate please call 770-415-9072
4172 & 3819 hwy 27 (both locations)
Riverdale Ga

That’s the info rest you can be creative ad shop logo
Flyer is back to school and barbershop themed

```html
<!DOCTYPE html>
<html lang="en">
<head>
<meta charset="utf-8">
<title>Copper Fade – 9th Annual Back 2 School Drive</title>
<link rel="stylesheet" href="https://fonts.googleapis.com/css2?family=Anton&family=Caveat:wght@500&family=Montserrat:wght@700;800&display=swap">
<style>
  :root {
    --paper: #ffffff;
    --ink: #111111;
    --night: #1b1b1b;
    --night-glow: #343434;
    --gold: #d6a419;
    --gold-deep: #9c7410;
    --red: #d1141c;
    --pink: #e8457a;
    --green: #5bb52a;
  }
  * { box-sizing: border-box; margin: 0; padding: 0; }
  html, body { width: 900px; height: 1200px; overflow: hidden; background: var(--paper); }
  .flyer { position: relative; width: 900px; height: 1200px; background: var(--paper); overflow: hidden; font-family: "Montserrat", sans-serif; }

  .header { position: absolute; left: 0; top: 0; width: 900px; height: 214px; display: flex; align-items: center; justify-content: center; }
  .shop-name { display: flex; align-items: center; gap: 18px; font-weight: 800; font-size: 58px; color: var(--ink); letter-spacing: 1px; text-transform: uppercase; }
  .shop-name .dot { width: 34px; height: 34px; border-radius: 50%; background: var(--red); }

  .edge { position: absolute; left: 0; top: 214px; width: 900px; height: 8px; background: var(--red); }

  .stage { position: absolute; left: 0; top: 222px; width: 900px; height: 853px; background: radial-gradient(ellipse at 45% 40%, var(--night-glow) 0%, var(--night) 70%); }

  .headline { position: absolute; left: 0; top: 232px; width: 900px; text-align: center; font-family: "Anton", sans-serif; font-size: 140px; line-height: 140px; letter-spacing: 2px; color: var(--gold); background: linear-gradient(180deg, #f0c231 0%, var(--gold) 45%, var(--gold-deep) 100%); -webkit-background-clip: text; background-clip: text; -webkit-text-fill-color: transparent; }
  .subhead { position: absolute; left: 0; top: 364px; width: 900px; text-align: center; font-family: "Caveat", cursive; font-weight: 500; font-size: 100px; line-height: 90px; color: var(--paper); }

  .date-pill { position: absolute; left: 139px; top: 465px; width: 623px; height: 83px; border-radius: 42px; background: var(--paper); display: flex; align-items: center; padding-left: 8px; gap: 22px; }
  .date-pill .badge { width: 68px; height: 68px; border-radius: 50%; background: var(--ink); display: flex; align-items: center; justify-content: center; }
  .date-pill .when { font-weight: 800; font-size: 31px; color: var(--ink); }

  .perks { position: absolute; left: 44px; top: 582px; list-style: none; }
  .perks li { display: flex; align-items: center; gap: 16px; height: 61px; font-weight: 800; font-size: 45px; color: var(--paper); }
  .perks .icon { width: 42px; height: 42px; border-radius: 50%; background: var(--gold); flex: none; display: flex; align-items: center; justify-content: center; }

  .tools-art { position: absolute; left: 730px; top: 566px; width: 170px; height: 216px; background: linear-gradient(160deg, var(--gold) 0%, var(--gold-deep) 100%); opacity: .85; border-radius: 14px 0 0 14px; }
  .supplies-art { position: absolute; left: 613px; top: 788px; width: 287px; height: 287px; background: linear-gradient(170deg, var(--green) 0%, #8a8d96 35%, #e5e5e5 60%, #4b4e57 85%, var(--pink) 100%); border-radius: 14px 0 0 0; }

  .contact { position: absolute; left: 47px; top: 896px; color: var(--paper); }
  .contact .call { margin-left: 31px; font-weight: 800; font-size: 23px; }
  .contact .phone { display: flex; align-items: center; gap: 10px; margin-top: 8px; font-weight: 800; font-size: 55px; line-height: 62px; }
  .contact .address { display: flex; align-items: center; gap: 12px; margin-top: 4px; font-weight: 800; font-size: 21px; text-transform: uppercase; }
  .contact .phone .icon { width: 44px; height: 44px; border-radius: 50%; background: var(--gold); display: flex; align-items: center; justify-content: center; }
  .contact .address .icon { width: 26px; height: 26px; margin-left: 8px; border-radius: 50%; background: var(--gold); display: flex; align-items: center; justify-content: center; }

  .footer { position: absolute; left: 0; top: 1075px; width: 900px; height: 118px; display: flex; align-items: center; justify-content: center; }
  .sponsor { font-weight: 800; font-size: 58px; color: var(--gold); letter-spacing: 1px; }
  .base-rule { position: absolute; left: 0; bottom: 0; width: 900px; height: 7px; background: var(--ink); }
</style>
</head>
<body>
<main class="flyer">
  <header class="header">
    <div class="shop-name"><span class="dot"></span>Copper Fade</div>
  </header>
  <div class="edge"></div>

  <section class="stage"></section>

  <h1 class="headline">9TH ANNUAL</h1>
  <p class="subhead">back 2 school drive</p>

  <div class="date-pill">
    <span class="badge">
      <svg width="36" height="36" viewBox="0 0 36 36" aria-hidden="true">
        <rect x="4" y="7" width="28" height="25" rx="3" fill="none" stroke="#fff" stroke-width="3"/>
        <line x1="4" y1="14" x2="32" y2="14" stroke="#fff" stroke-width="3"/>
        <line x1="11" y1="3" x2="11" y2="10" stroke="#fff" stroke-width="3"/>
        <line x1="25" y1="3" x2="25" y2="10" stroke="#fff" stroke-width="3"/>
        <g fill="#fff"><rect x="9" y="18" width="4" height="4"/><rect x="16" y="18" width="4" height="4"/><rect x="23" y="18" width="4" height="4"/><rect x="9" y="25" width="4" height="4"/><rect x="16" y="25" width="4" height="4"/></g>
      </svg>
    </span>
    <span class="when">SATURDAY JULY 31 12–5PM</span>
  </div>

  <ul class="perks">
    <li><span class="icon"><svg width="22" height="22" viewBox="0 0 22 22" aria-hidden="true"><path d="M2 10 L11 3 L20 10 V20 H2 Z" fill="#fff"/><rect x="9" y="14" width="4" height="6" fill="#d6a419"/></svg></span>FREE SCHOOL SUPPLIES</li>
    <li><span class="icon"><svg width="24" height="16" viewBox="0 0 24 16" aria-hidden="true"><rect x="1" y="2" width="22" height="12" rx="6" fill="#fff"/><circle cx="17" cy="8" r="2" fill="#d6a419"/><rect x="5" y="7" width="6" height="2" fill="#d6a419"/><rect x="7" y="5" width="2" height="6" fill="#d6a419"/></svg></span>GAMES</li>
    <li><span class="icon"><svg width="22" height="22" viewBox="0 0 22 22" aria-hidden="true"><circle cx="11" cy="11" r="8" fill="#fff"/><circle cx="8" cy="9" r="1.5" fill="#d6a419"/><circle cx="14" cy="9" r="1.5" fill="#d6a419"/><path d="M7 13 Q11 17 15 13" stroke="#d6a419" stroke-width="1.8" fill="none"/></svg></span>ENTERTAINMENT</li>
    <li><span class="icon"><svg width="24" height="20" viewBox="0 0 24 20" aria-hidden="true"><path d="M3 9 Q12 0 21 9 Z" fill="#fff"/><rect x="3" y="11" width="18" height="3" fill="#fff"/><path d="M3 16 H21 Q21 19 18 19 H6 Q3 19 3 16 Z" fill="#fff"/></svg></span>FREE FOOD</li>
  </ul>

  <div class="tools-art" role="img" aria-label="Gold comb and scissors barbershop illustration"></div>
  <div class="supplies-art" role="img" aria-label="Photo of a stack of books and notebooks with a green apple, pencils and scissors"></div>

  <div class="contact">
    <p class="call">TO VOLUNTEER OR DONATE PLEASE CALL</p>
    <p class="phone"><span class="icon"><svg width="22" height="22" viewBox="0 0 24 24" aria-hidden="true"><path d="M6.6 10.8a15.2 15.2 0 0 0 6.6 6.6l2.2-2.2a1 1 0 0 1 1-.25 11.4 11.4 0 0 0 3.6.57 1 1 0 0 1 1 1V20a1 1 0 0 1-1 1A17 17 0 0 1 3 4a1 1 0 0 1 1-1h3.5a1 1 0 0 1 1 1c0 1.25.2 2.45.57 3.570a1 1 0 0 1-.25 1z" fill="#1b1b1b"/></svg></span>770-415-9072</p>
    <p class="address"><span class="icon"><svg width="14" height="16" viewBox="0 0 14 18" aria-hidden="true"><path d="M7 1a5.5 5.5 0 0 0-5.5 5.5C1.5 11 7 17 7 17s5.5-6 5.5-10.5A5.5 5.5 0 0 0 7 1z" fill="#1b1b1b"/><circle cx="7" cy="6.5" r="2" fill="#d6a419"/></svg></span>4172 &amp; 3819 hwy 27 Riverdale GA</p>
  </div>

  <footer class="footer">
    <span class="sponsor">Twist Pad</span>
  </footer>
  <div class="base-rule"></div>
</main>
</body>
</html>
```